design a construction company business card

Design business card around our logo. Card must have all the typical info: name, title, address, phone, email, business name, etc. Somewhere on the card I would like to see our motto "Built on integrity... Inspired by commitment." Consider adding a splash of bright orange to the card to complement the blues and silvers/grays in the logo. We are open to metallic inks, textures, etc. We would like to see options on both light and dark backgrounds. The font in the logo is Euro Technic Extended Regular.

```html
<!DOCTYPE html>
<html lang="en">
<head>
<meta charset="utf-8">
<title>Halvorsen Builders – Business Card</title>
<link href="https://fonts.googleapis.com/css2?family=Lato:ital,wght@0,400;0,700;1,400&display=swap" rel="stylesheet">
<style>
  :root {
    --page-bg: #d9dbdf;
    --card-black: #121212;
    --brand-blue: #2f7bd6;
    --band-blue: #2a6ed0;
    --accent-orange: #f58220;
    --text-grey: #c9c9cc;
    --text-white: #ffffff;
    --divider: #4a4a4e;
    --back-top: #1f7fd0;
    --back-bottom: #2c45a8;
  }
  * { box-sizing: border-box; margin: 0; padding: 0; }
  html, body {
    width: 1200px; height: 782px; overflow: hidden;
    background: var(--page-bg);
    font-family: "Lato", Arial, sans-serif;
  }
  .stage { position: relative; width: 1200px; height: 782px; }
  .card {
    position: absolute; width: 540px; height: 309px;
    top: 237px; border-radius: 2px; overflow: hidden;
    box-shadow: 0 10px 24px rgba(0,0,0,.25);
  }
  .card--front { left: 40px; background: var(--card-black); }
  .card--back {
    left: 620px;
    background: linear-gradient(180deg, var(--back-top), var(--back-bottom));
  }
  .front__accent {
    position: absolute; left: 0; right: 0; bottom: 9px; height: 3px;
    background: var(--accent-orange);
  }
  .front__band {
    position: absolute; left: 0; right: 0; bottom: 0; height: 9px;
    background: var(--band-blue);
  }
  .company {
    position: absolute; left: 30px; top: 118px; width: 200px;
    text-align: center; color: var(--brand-blue);
    font-weight: 700; text-transform: uppercase;
  }
  .company__name { font-size: 27px; letter-spacing: 2px; line-height: 1.1; }
  .company__sub { font-size: 12px; letter-spacing: 2.4px; margin-top: 4px; }
  .divider {
    position: absolute; left: 258px; top: 70px; width: 1px; height: 160px;
    background: var(--divider);
  }
  .contact {
    position: absolute; left: 282px; top: 82px;
    color: var(--text-grey); text-transform: uppercase;
  }
  .contact__name {
    color: var(--brand-blue); font-weight: 700;
    font-size: 17px; letter-spacing: 1px;
  }
  .contact__title { font-size: 12px; letter-spacing: 1.4px; margin-bottom: 8px; }
  .contact__line {
    display: flex; align-items: center; gap: 7px;
    font-size: 13.5px; letter-spacing: .8px; line-height: 20px;
  }
  .contact__line svg { width: 11px; height: 11px; flex: none; }
  .contact__address {
    font-size: 13.5px; letter-spacing: .8px; line-height: 18px; margin-top: 4px;
  }
  .back__motto {
    position: absolute; left: 0; right: 0; top: 196px;
    text-align: center; color: var(--text-white);
    font-size: 14px; font-style: italic; letter-spacing: .6px;
  }
  .back__rule {
    position: absolute; left: 210px; width: 120px; top: 186px; height: 2px;
    background: var(--accent-orange);
  }
</style>
</head>
<body>
<div class="stage">
  <section class="card card--front" aria-label="Business card front">
    <div class="company">
      <div class="company__name">Halvorsen</div>
      <div class="company__sub">Builders, Inc.</div>
    </div>
    <div class="divider"></div>
    <div class="contact">
      <div class="contact__name">Marcus Ellery</div>
      <div class="contact__title">Managing Director</div>
      <div class="contact__line">
        <svg viewBox="0 0 12 12" aria-hidden="true"><path fill="var(--brand-blue)" d="M2.5 1h2l1 3-1.3 1a7 7 0 0 0 2.8 2.8l1-1.3 3 1v2a1 1 0 0 1-1 1A10 10 0 0 1 1.5 2a1 1 0 0 1 1-1z"/></svg>
        055-318 720 446
      </div>
      <div class="contact__line">
        <svg viewBox="0 0 12 12" aria-hidden="true"><rect x="1" y="2.5" width="10" height="7" fill="var(--brand-blue)"/><path d="M1 2.5l5 4 5-4" fill="none" stroke="var(--card-black)" stroke-width="1"/></svg>
        info@halvorbuild.com
      </div>
      <div class="contact__line">
        <svg viewBox="0 0 12 12" aria-hidden="true"><circle cx="6" cy="6" r="5" fill="var(--brand-blue)"/><path d="M1 6h10M6 1c2 2.5 2 7.5 0 10M6 1c-2 2.5-2 7.5 0 10" fill="none" stroke="var(--card-black)" stroke-width=".8"/></svg>
        www.halvorbuild.com
      </div>
      <div class="contact__address">88 Foundry Road<br>Brookvale, 30417</div>
    </div>
    <div class="front__accent"></div>
    <div class="front__band"></div>
  </section>

  <section class="card card--back" aria-label="Business card back">
    <div class="back__rule"></div>
    <p class="back__motto">Built on integrity... Inspired by commitment.</p>
  </section>
</div>
</body>
</html>
```